Business Card Design for Irrigation Contractor

Design and layout for company business cards to include the following information:
1. Logo
2. Installation \ Service \ Maintenance
3. U-47283
4. Walter J. Lindqvist
5. walter@7Kirrigation.com
6. Office 555-712-9364
7. Cell 555-286-0517

```html
<!DOCTYPE html>
<html lang="en">
<head>
<meta charset="utf-8">
<title>7K Irrigation – Business Card</title>
<link rel="stylesheet" href="https://fonts.googleapis.com/css2?family=Montserrat:wght@400;500;700;800&display=swap">
<style>
  :root {
    --page-bg: #e9ebee;
    --navy-deep: #0a2f58;
    --blue-mid: #155697;
    --blue-bright: #1a72bd;
    --accent-blue: #1b6bb3;
    --ink: #1d3552;
    --wordmark: #0d3a66;
    --white: #ffffff;
    --mark-light: #dfe4ea;
    --mark-blue: #3aa0df;
    --rule: #4a4f57;
  }
  * { box-sizing: border-box; margin: 0; padding: 0; }
  html, body {
    width: 1200px; height: 1050px; overflow: hidden;
    background: var(--page-bg);
    font-family: "Montserrat", sans-serif;
  }
  .sheet { position: relative; width: 1200px; height: 1050px; }
  .card {
    position: absolute; left: 240px; width: 720px; height: 411px;
    overflow: hidden;
    box-shadow: 0 6px 18px rgba(0,0,0,0.18);
  }
  .card--front {
    top: 94px;
    background: linear-gradient(90deg, var(--navy-deep) 0%, var(--blue-mid) 30%, var(--blue-bright) 46%, var(--blue-mid) 64%, var(--navy-deep) 100%);
    color: var(--white);
    text-align: center;
  }
  .front-arc { position: absolute; inset: 0; }
  .front-mark {
    position: absolute; left: 314px; top: 112px;
    width: 92px; height: 92px; border-radius: 50%;
    background: var(--mark-light);
  }
  .front-name {
    position: absolute; left: 0; right: 0; top: 262px;
    font-weight: 800; font-size: 46px; letter-spacing: 0.5px; line-height: 1;
  }
  .front-tagline {
    position: absolute; left: 0; right: 0; top: 316px;
    font-weight: 500; font-size: 20px; letter-spacing: 0.8px;
  }
  .front-license {
    position: absolute; left: 0; right: 0; top: 370px;
    font-weight: 700; font-size: 16px; letter-spacing: 0.5px;
  }
  .card--back { top: 545px; background: var(--white); }
  .back-mark {
    position: absolute; left: 152px; top: 150px;
    width: 72px; height: 72px; border-radius: 50%;
    background: var(--mark-blue);
  }
  .back-name {
    position: absolute; left: 60px; width: 255px; top: 246px;
    text-align: center;
    font-weight: 800; font-size: 25px; color: var(--wordmark); line-height: 1;
  }
  .divider {
    position: absolute; left: 369px; top: 147px;
    width: 1.5px; height: 126px; background: var(--rule);
  }
  .person {
    position: absolute; left: 414px; top: 142px;
    font-weight: 700; font-size: 23px; color: var(--accent-blue);
    text-transform: uppercase; letter-spacing: 0.2px;
  }
  .contacts {
    position: absolute; left: 414px; top: 184px;
    list-style: none; color: var(--ink);
    font-size: 17px; font-weight: 400; letter-spacing: 0.3px;
  }
  .contacts li { display: flex; align-items: center; height: 22.5px; }
  .contacts svg { width: 17px; height: 17px; margin-right: 6px; flex: none; }
</style>
</head>
<body>
<main class="sheet">
  <section class="card card--front">
    <svg class="front-arc" viewBox="0 0 720 411" aria-hidden="true">
      <path d="M100 0 C 330 120, 300 300, 300 411 L 720 411 L 720 0 Z" fill="rgba(255,255,255,0.04)"/>
      <path d="M570 0 C 590 140, 540 300, 420 411 L 720 411 L 720 0 Z" fill="rgba(255,255,255,0.03)"/>
    </svg>
    <div class="front-mark" aria-hidden="true"></div>
    <h1 class="front-name">7K IRRIGATION</h1>
    <p class="front-tagline">Installation \ Service \ Maintenance</p>
    <p class="front-license">U-47283</p>
  </section>

  <section class="card card--back">
    <div class="back-mark" aria-hidden="true"></div>
    <p class="back-name">7K IRRIGATION</p>
    <div class="divider" aria-hidden="true"></div>
    <h2 class="person">Walter J. Lindqvist</h2>
    <ul class="contacts">
      <li>
        <svg viewBox="0 0 20 20" aria-hidden="true"><circle cx="10" cy="10" r="8.8" fill="none" stroke="#1b6bb3" stroke-width="1.6"/><path d="M7 5.5l1.6 2.4-1 1.1c.7 1.5 1.8 2.6 3.3 3.3l1.1-1 2.4 1.6-.8 1.8c-3.6-.3-6.9-3.6-7.2-7.2z" fill="#1d3552"/></svg>
        555-286-0517
      </li>
      <li>
        <svg viewBox="0 0 20 20" aria-hidden="true"><circle cx="10" cy="10" r="8.8" fill="none" stroke="#1b6bb3" stroke-width="1.6"/><rect x="5.5" y="8" width="9" height="6" rx="1" fill="#1d3552"/><path d="M5 7.5c3-2 7-2 10 0" stroke="#1d3552" stroke-width="1.6" fill="none"/><circle cx="10" cy="11" r="1.3" fill="#fff"/></svg>
        555-712-9364
      </li>
      <li>
        <svg viewBox="0 0 20 20" aria-hidden="true"><circle cx="10" cy="10" r="8.8" fill="none" stroke="#1b6bb3" stroke-width="1.6"/><rect x="5.5" y="7" width="9" height="6.5" rx="0.8" fill="#1d3552"/><path d="M5.8 7.5l4.2 3 4.2-3" stroke="#fff" stroke-width="1" fill="none"/></svg>
        walter@7Kirrigation.com
      </li>
      <li>
        <svg viewBox="0 0 20 20" aria-hidden="true"><circle cx="10" cy="10" r="8.8" fill="none" stroke="#1b6bb3" stroke-width="1.6"/><circle cx="10" cy="10" r="4.5" fill="none" stroke="#1d3552" stroke-width="1"/><path d="M5.5 10h9M10 5.5v9M7.8 6c-1.4 2.6-1.4 5.4 0 8M12.2 6c1.4 2.6 1.4 5.4 0 8" stroke="#1d3552" stroke-width="0.9" fill="none"/></svg>
        7Kirrigation.com
      </li>
    </ul>
  </section>
</main>
</body>
</html>
```